Management Consultancy needs sharp professional services showcased in a brochure

We are a management consultancy specializing on contract management and conflict avoidance services requiring a professional brochure showcasing our services to prospective clients.

Attached are a selection of existing stationary and the colour scheme.

Further details on our company can be found at www.velmor-advisory-partners.com
Updates

Preference is for bi-fold, however, innovative tri-fold will be considered. Added Monday, August 7, 2017

Target Market(s)

Construction companies, consultants, developers, oil and gas service providers, NGO's, SME's.

Industry/Entity Type

Management

Requirements
Must have
• High degree of professionalism with eye catching, sharp detail. No frils.
• Colour scheme as per the attachments
• Font as per attachments - Century Gothic
• Details of our company and services
Nice to have
• Open to ideas, thinking along the lines of a car brochure type design.
• Bi-fold preferred, by trifold accepted if innovative.
Should not have
• Remove reference to the United Arab Emirates.
• No cartoon/clipart photos.

```html
<!DOCTYPE html>
<html lang="en">
<head>
<meta charset="utf-8">
<title>Velmor Advisory – Contract &amp; Conflict Advisory Brochure</title>
<link href="https://fonts.googleapis.com/css2?family=Marcellus+SC&family=Questrial&display=swap" rel="stylesheet">
<style>
  :root {
    --backdrop: #6f6f6f;
    --paper: #ffffff;
    --paper-shade: #ececec;
    --brand-red: #c8161f;
    --brand-red-deep: #8e0810;
    --brand-navy: #2c4a6e;
    --ink-navy: #23406a;
    --ink-body: #3c3c3c;
    --ink-light: #ffffff;
  }
  html, body {
    margin: 0;
    width: 1200px;
    height: 1200px;
    overflow: hidden;
    background: var(--backdrop);
  }
  .spread {
    position: absolute;
    left: 50px;
    top: 208px;
    width: 963px;
    height: 686px;
    transform: scale(1.1423);
    transform-origin: top left;
    background: var(--paper);
    overflow: hidden;
    font-family: "Questrial", "Century Gothic", sans-serif;
  }
  .spread-art {
    position: absolute;
    inset: 0;
    width: 963px;
    height: 686px;
  }
  .services {
    position: absolute;
    top: 28px;
    color: var(--ink-body);
  }
  .services--conflict { left: 29px; width: 250px; }
  .services--contract { left: 284px; top: 38px; width: 170px; }
  .services__heading {
    margin: 0;
    font-family: "Marcellus SC", serif;
    font-weight: 400;
    font-size: 22px;
    line-height: 1;
    color: var(--brand-red);
  }
  .services__group {
    margin: 5px 0 4px;
    font-size: 13.5px;
    font-weight: 700;
    color: var(--ink-navy);
  }
  .services--contract .services__group { margin-top: 0; }
  .services__list {
    margin: 0;
    padding: 0 0 0 16px;
    list-style: none;
    font-size: 10.5px;
    line-height: 15.5px;
  }
  .services__list li { position: relative; }
  .services__list li::before {
    content: "";
    position: absolute;
    left: -11px;
    top: 5.5px;
    width: 4px;
    height: 4px;
    border-radius: 50%;
    background: var(--brand-red);
  }
  .brand-name {
    position: absolute;
    font-family: "Questrial", "Century Gothic", sans-serif;
    white-space: nowrap;
  }
  .brand-name--cover {
    left: 604px;
    width: 290px;
    top: 102px;
    text-align: center;
    font-size: 23px;
    color: var(--ink-navy);
  }
  .brand-name--back {
    left: 296px;
    top: 506px;
    font-size: 14px;
    color: var(--ink-light);
  }
  .cover-title {
    position: absolute;
    left: 520px;
    width: 440px;
    top: 210px;
    margin: 0;
    text-align: center;
    font-family: "Marcellus SC", serif;
    font-weight: 400;
    color: var(--ink-light);
    line-height: 1.2;
  }
  .cover-title__line1 { display: block; font-size: 37px; }
  .cover-title__line2 { display: block; font-size: 39px; }
  .contact {
    position: absolute;
    left: 279px;
    top: 532px;
    margin: 0;
    padding: 0;
    list-style: none;
    font-size: 11.5px;
    line-height: 16.3px;
    color: var(--ink-light);
  }
  .contact li { display: flex; align-items: center; gap: 8px; }
  .contact svg { width: 10px; height: 10px; fill: var(--ink-light); flex: none; }
</style>
</head>
<body>
  <div class="spread">
    <svg class="spread-art" viewBox="0 0 963 686" aria-hidden="false">
      <defs>
        <linearGradient id="cover-shade" x1="0" y1="0" x2="1" y2="0">
          <stop offset="0" stop-color="#e6e6e6"/>
          <stop offset="0.35" stop-color="#f7f7f7"/>
          <stop offset="1" stop-color="#ffffff"/>
        </linearGradient>
        <linearGradient id="red-sweep" x1="0" y1="0" x2="1" y2="0">
          <stop offset="0" stop-color="#d11a24"/>
          <stop offset="0.55" stop-color="#c0131c"/>
          <stop offset="1" stop-color="#8e0810"/>
        </linearGradient>
        <linearGradient id="meeting-tones" x1="0" y1="0" x2="1" y2="1">
          <stop offset="0" stop-color="#dfe9ef"/>
          <stop offset="0.5" stop-color="#9fb6c9"/>
          <stop offset="1" stop-color="#2a3c5c"/>
        </linearGradient>
        <linearGradient id="consultant-tones" x1="0" y1="0" x2="0" y2="1">
          <stop offset="0" stop-color="#c9b3a4"/>
          <stop offset="0.3" stop-color="#3b4256"/>
          <stop offset="1" stop-color="#14161f"/>
        </linearGradient>
      </defs>

      <rect class="cover-panel" x="484" y="0" width="479" height="686" fill="url(#cover-shade)"/>

      <path class="swoosh-navy" fill="var(--brand-navy)"
            d="M575 154 C390 172 215 280 145 425 L40 686 L110 686 L182 440 C255 300 400 195 575 154 Z"/>

      <path class="swoosh-red" fill="url(#red-sweep)"
            d="M575 154 C420 195 262 305 182 440 L150 686 L481 686 C525 520 700 378 963 365 L963 195 C830 162 700 150 575 154 Z"/>

      <path class="photo-meeting" role="img" aria-label="Photo: consultants shaking hands across a desk with a laptop"
            fill="url(#meeting-tones)"
            d="M481 686 C525 520 700 378 963 365 L963 686 Z"/>
      <path class="photo-edge" fill="none" stroke="#ffffff" stroke-width="5"
            d="M481 686 C525 520 700 378 963 365"/>

      <path class="photo-consultant" role="img" aria-label="Photo: smiling young consultant in a suit giving a thumbs up"
            fill="url(#consultant-tones)"
            d="M62 300 C62 272 100 258 120 262 C150 268 162 300 150 360 C200 380 240 400 256 430 L258 686 L0 686 L0 420 C20 400 40 385 70 365 C60 345 58 320 62 300 Z"/>
    </svg>

    <section class="services services--conflict">
      <h2 class="services__heading">Our Services</h2>
      <h3 class="services__group">Conflict Advisory</h3>
      <ul class="services__list">
        <li>Restoration and Mediation Services</li>
        <li>Shuttle Diplomacy Services and In Persona Intermediary Services</li>
        <li>Negotiation Support Services</li>
        <li>Workplace Mediation Services</li>
      </ul>
    </section>

    <section class="services services--contract">
      <h3 class="services__group">Contract Advisory</h3>
      <ul class="services__list">
        <li>Contract Troubleshooting</li>
        <li>Contracts Audit Services and Performance Management</li>
        <li>Strategic Review &amp; Risk Assessment</li>
        <li>Contract Fraud Investigation</li>
      </ul>
    </section>

    <div class="brand-name brand-name--cover">Velmor Advisory</div>

    <h1 class="cover-title">
      <span class="cover-title__line1">The Contract &amp;</span>
      <span class="cover-title__line2">Conflict Advisory</span>
    </h1>

    <div class="brand-name brand-name--back">Velmor Advisory</div>
    <ul class="contact">
      <li><svg viewBox="0 0 10 10"><path d="M2 0.5 L3.5 0.5 L4.3 2.8 L3.2 3.6 C3.8 5 5 6.2 6.4 6.8 L7.2 5.7 L9.5 6.5 L9.5 8 C9.5 9 8.8 9.5 8 9.5 C4 9.2 0.8 6 0.5 2 C0.5 1.2 1 0.5 2 0.5 Z"/></svg>your ph no. goes here</li>
      <li><svg viewBox="0 0 10 10"><path d="M0.5 2 L9.5 2 L9.5 8.5 L0.5 8.5 Z M1.2 2.6 L5 5.6 L8.8 2.6 Z" fill-rule="evenodd"/></svg>your mail address goes here</li>
      <li><svg viewBox="0 0 10 10"><path d="M5 0.5 A4.5 4.5 0 1 0 5 9.5 A4.5 4.5 0 1 0 5 0.5 Z M5 1.5 A3.5 3.5 0 1 1 5 8.5 A3.5 3.5 0 1 1 5 1.5 Z M1.5 4.6 L8.5 4.6 L8.5 5.4 L1.5 5.4 Z M4.6 1.5 L5.4 1.5 L5.4 8.5 L4.6 8.5 Z" fill-rule="evenodd"/></svg>www.velmor-advisory-partners.com</li>
      <li><svg viewBox="0 0 10 10"><path d="M5 0.5 C3 0.5 1.8 2 1.8 3.7 C1.8 6 5 9.5 5 9.5 C5 9.5 8.2 6 8.2 3.7 C8.2 2 7 0.5 5 0.5 Z M5 2.5 A1.2 1.2 0 1 1 5 4.9 A1.2 1.2 0 1 1 5 2.5 Z" fill-rule="evenodd"/></svg>your address goes here</li>
    </ul>
  </div>
</body>
</html>
```